Book cover design for a book named FLINT

Hello Designers,
The name of the book is FLINT and it is about unexpected experiences individuals have which are beyond their control. Occurrences they are unable to overcome or get out of themselves without the help of God. After overcoming these situations they know only God could have done this for them, no one else could have. It is an adult Christian book. I would like you to be as creative as you can with the cover, using color, light, graphic designs, shapes, scale, lines etc. (you are the designers, I don't know how to do these things.) I would like to use the image created on a paperback, hardcover or e book. I tried to use an image from Framelodge just to give you some idea of my thinking but you do not have to use these hands. The hands should look as if they are giving someone the word TESTIMONY not receiving it. Use of the words provided, the light rays, and some type of hands extended should not change, but how you use them is up to you. Use the words, light rays, and hands however you wish as long as they convey someone giving the word TESTIMONY. The word TESTIMONY should be proportional to the hand in size and should appear as if being held in the actual hand it should not be larger than the book name. It is a Christian book of testimonies. Also for your design samples you can use the name Melissa Trent for the author. Thank you, please feel free to contact me if you have any questions. I am looking for the cover to be an attention grabber and give the reader something to really think about and remember visually when they see this cover. Thank you again.

Target Market(s)

anyone and christians

Requirements
Must have
• Use of the words provided, the light rays, and some type of hands extended should not change.
Nice to have
• be as creative as you can with the cover, using color, light, graphic designs, shapes, scale, lines etc. (you are the designers, I don't know how to do these things.)
Should not have
• It should not have fonts, colors, etc. that convey it is a child's book, fairytale, or fictional etc. It is a book of true stories that actually happened. It should not look exactly like my example, what I provided.

```html
<!DOCTYPE html>
<html lang="en">
<head>
<meta charset="utf-8">
<title>FLINT – Book Cover</title>
<link href="https://fonts.googleapis.com/css2?family=Cinzel:wght@700;900&family=Oswald:wght@700&family=Arimo:wght@400;700&display=swap" rel="stylesheet">
<style>
  :root {
    --page: #ffffff;
    --cover: #030303;
    --gold-light: #fff2b8;
    --gold-mid: #e0b452;
    --gold-deep: #8a5a14;
    --white: #ffffff;
    --red: #d4080c;
    --glow: #fff6d8;
    --ray: #f3c766;
    --hands: #5a4636;
  }
  html, body {
    margin: 0;
    width: 1200px;
    height: 1200px;
    overflow: hidden;
    background: var(--page);
  }
  .cover {
    position: absolute;
    left: 252px;
    top: 52px;
    width: 720px;
    height: 1080px;
    background: var(--cover);
    overflow: hidden;
    text-align: center;
  }
  .title {
    position: absolute;
    left: 0;
    width: 100%;
    font-family: "Cinzel", serif;
    font-weight: 900;
    font-size: 196px;
    line-height: 1;
    letter-spacing: 4px;
    margin: 0;
  }
  .title-main {
    top: 78px;
    background: linear-gradient(180deg, var(--gold-light) 0%, var(--gold-mid) 38%, var(--gold-deep) 62%, var(--gold-mid) 80%, var(--gold-light) 100%);
    -webkit-background-clip: text;
    background-clip: text;
    color: transparent;
    filter: drop-shadow(0 0 14px rgba(224, 180, 82, 0.35));
  }
  .title-reflection {
    top: 250px;
    transform: scaleY(-1);
    color: var(--gold-deep);
    opacity: 0.55;
    -webkit-mask-image: linear-gradient(0deg, rgba(0,0,0,0.8) 0%, rgba(0,0,0,0) 45%);
    mask-image: linear-gradient(0deg, rgba(0,0,0,0.8) 0%, rgba(0,0,0,0) 45%);
  }
  .tagline {
    position: absolute;
    top: 286px;
    left: 0;
    width: 100%;
    margin: 0;
    font-family: "Arimo", sans-serif;
    font-size: 32px;
    line-height: 50px;
    color: var(--white);
  }
  .tagline strong { font-weight: 700; }
  .artwork {
    position: absolute;
    left: 70px;
    top: 480px;
    width: 580px;
    height: 500px;
    background:
      radial-gradient(ellipse 34% 14% at 50% 82%, var(--hands) 0%, rgba(90,70,54,0.6) 60%, rgba(90,70,54,0) 100%),
      radial-gradient(ellipse 22% 12% at 50% 62%, var(--glow) 0%, rgba(255,246,216,0.7) 45%, rgba(255,246,216,0) 100%),
      radial-gradient(ellipse 48% 60% at 50% 65%, rgba(243,199,102,0.55) 0%, rgba(243,199,102,0.15) 55%, rgba(0,0,0,0) 80%);
  }
  .gift-line {
    position: absolute;
    left: 0;
    width: 100%;
    margin: 0;
    font-family: "Oswald", sans-serif;
    font-weight: 700;
    color: var(--red);
    text-transform: uppercase;
  }
  .gift-line.small {
    font-size: 42px;
    line-height: 48px;
    top: 592px;
    letter-spacing: 1px;
  }
  .gift-line.big {
    top: 690px;
    font-size: 116px;
    line-height: 1;
    letter-spacing: 2px;
    transform: scaleY(1.12);
  }
  .author {
    position: absolute;
    left: 0;
    width: 100%;
    top: 984px;
    margin: 0;
    font-family: "Arimo", sans-serif;
    font-weight: 700;
    font-size: 52px;
    color: var(--white);
  }
</style>
</head>
<body>
  <main class="cover">
    <h1 class="title title-main">FLINT</h1>
    <div class="title title-reflection" aria-hidden="true">FLINT</div>

    <p class="tagline">
      BEFORE THERE WILL EVER BE<br>
      A <strong>TESTIMONY</strong><br>
      THERE MUST ALWAYS BE<br>
      AN <strong>EXPERIENCE</strong>
    </p>

    <div class="artwork" role="img" aria-label="Golden light rays bursting upward from a pair of open, outstretched hands offering a glowing light"></div>

    <p class="gift-line small">Out of this test I’ve<br>given you a</p>
    <p class="gift-line big">Testimony</p>

    <p class="author">MELISSA TRENT</p>
  </main>
</body>
</html>
```